Introduction:
We are an Australia-based Cyber Security Penetration testing company seeking a website redesign to showcase our services, expertise, and experience. Our target audience includes businesses and organizations of all sizes who are seeking to secure their IT infrastructure against cyber threats. The purpose of the website redesign is to increase our online presence, generate leads, and establish our company as a trusted authority in the industry.
Objectives:
Create a professional and modern website that is easy to navigate and user-friendly.
Provide information about our company, services, and expertise.
Clearly display table of our 3 services: Bug Bounty as a Service, Penetration Testing and Code Review.
Generate leads through online contact forms and calls-to-action.
Optimize the website for search engines to increase visibility and traffic.
Website similar to: https://www.velmoro.com.au/.
Target Audience:
Our target audience includes businesses and organizations of all sizes that require cybersecurity penetration testing services. These include:
Small and medium-sized enterprises (SMEs)
Australian Government agencies
Design Requirements:
Clean, modern, and professional design.
Use of colors that convey trust, reliability, and expertise (such as orange and grey).
Calls-to-action that encourage visitors to contact us or request a quote.
Integration with social media channels to increase engagement and brand awareness.
A blog section to showcase our thought leadership and expertise.
A news section to share updates about our company and the industry.
Content Requirements:
Home page that introduces our company and services and highlights our expertise.
About Us page that provides information about our company, team, and values.
Services page that lists our services and explains the benefits of each.
Case Studies page that showcases our previous work and success stories.
Contact Us page that includes a contact form, phone number, and email address.
Blog section with articles related to the cybersecurity industry and our services.
News section with updates about our company and the industry.

```html
<!DOCTYPE html>
<html lang="en">
<head>
<meta charset="utf-8">
<title>Emberstrata – Cyber Security Penetration Testing</title>
<link href="https://fonts.googleapis.com/css2?family=Montserrat:wght@400;500;600;700&family=Poppins:wght@600;700&display=swap" rel="stylesheet">
<style>
:root{
  --orange:#ee5a2c;
  --ink:#333a40;
  --text:#5d6165;
  --dark:#0b1820;
  --darker:#05090c;
  --light:#f3f3f3;
  --white:#ffffff;
  --line:#d9d9d9;
}
*{box-sizing:border-box;margin:0;padding:0}
html,body{width:1200px;height:3901px;overflow:hidden;background:var(--white)}
body{position:relative;font-family:"Montserrat",sans-serif;color:var(--text)}
.abs{position:absolute}
.btn{position:absolute;height:33px;border:2px solid var(--ink);border-radius:17px;color:var(--orange);font-size:10px;font-weight:700;display:flex;align-items:center;justify-content:center;letter-spacing:.3px;background:transparent}
.btn.on-dark{border-color:var(--white)}
.heading{position:absolute;font-family:"Poppins",sans-serif;font-weight:600;font-size:36px;color:var(--ink);line-height:1}
.heading span{color:var(--orange)}
.heading.light{color:var(--white)}
.rule{position:absolute;width:56px;height:3px;background:var(--orange)}
.para{position:absolute;font-size:11.5px;line-height:20.5px;text-align:justify}
/* hero */
.hero{left:81px;top:9px;width:1026px;height:615px;background:radial-gradient(circle at 72% 40%,#1f8e9c 0%,#145463 25%,#0c2b36 55%,#08161d 100%)}
.brand{position:absolute;font-family:"Montserrat",sans-serif;font-weight:700;color:var(--white)}
.nav{position:absolute;top:48px;display:flex;gap:28px;left:448px;font-size:11px;color:var(--white);font-weight:500}
.hero-title{left:203px;top:258px;font-family:"Poppins",sans-serif;font-weight:700;font-size:60px;color:var(--white);line-height:1}
.hero-sub{left:203px;top:332px;font-size:13px;font-weight:700;color:var(--white)}
.slider-line{left:81px;top:572px;width:99px;height:2px;background:var(--white)}
.dot{position:absolute;width:9px;height:9px;border-radius:50%;background:var(--white);top:568px}
/* services */
.services{left:81px;top:1130px;width:1026px;height:715px;background:linear-gradient(180deg,#09151c 0%,#0d1f29 70%,#12232b 100%)}
.card-frame{position:absolute;border:2px solid var(--white);border-top:none}
.card-top{position:absolute;height:2px;background:var(--white)}
.card-title{position:absolute;width:246px;text-align:center;color:var(--white);font-weight:700;font-size:16.5px}
.card-text{position:absolute;width:190px;text-align:center;color:#dfe3e5;font-size:11px;line-height:20.5px}
.ring{position:absolute;width:110px;height:110px;border-radius:50%;border:3px solid var(--white);background:var(--dark);display:flex;align-items:center;justify-content:center}
.ring .core{width:86px;height:86px;border-radius:50%;background:var(--orange);display:flex;align-items:center;justify-content:center}
.side-dot{position:absolute;width:12px;height:12px;border-radius:50%;background:var(--orange);border:2px solid var(--white)}
/* expertise */
.expertise-bg{left:81px;top:1845px;width:1026px;height:440px;background:var(--light)}
/* news */
.news-big{left:204px;top:2469px;width:389px;height:360px;background:linear-gradient(160deg,#1b3c5a,#0e1f30 60%,#0a1520)}
.badge{position:absolute;height:20px;padding:0 10px;border-radius:10px;background:var(--orange);color:var(--white);font-size:9.5px;font-weight:600;display:flex;align-items:center;gap:4px}
.news-card{position:absolute;left:602px;width:382px;height:173px;border:1px solid #f2a58c;background:var(--white)}
.news-thumb{position:absolute;left:0;top:0;width:153px;height:171px;background:linear-gradient(150deg,#2c4f70,#10243a)}
.news-card h3{position:absolute;left:170px;top:54px;width:195px;font-size:14.5px;line-height:20px;font-weight:700;color:var(--ink)}
.news-card p{position:absolute;left:170px;top:102px;width:195px;font-size:9.5px;line-height:16.5px;color:var(--text)}
/* contact */
.contact-bg{left:81px;top:2941px;width:1026px;height:576px;background:linear-gradient(180deg,#f4f4f4,#ebebeb)}
.field{position:absolute;border:1px solid var(--line);background:var(--white);font-size:9px;color:#777;padding:10px 14px}
/* footer */
.footer{left:81px;top:3517px;width:1026px;height:338px;background:linear-gradient(180deg,#050709,#0c1115)}
.col-head{position:absolute;top:3556px;color:var(--white);font-weight:700;font-size:17px}
.links{position:absolute;top:3595px;list-style:none;color:#d5d5d5;font-size:11px;line-height:20.5px}
.social{position:absolute;top:3681px;width:26px;height:26px;border-radius:50%;background:var(--white);display:flex;align-items:center;justify-content:center}
.social i{width:8px;height:8px;border-radius:50%;background:var(--orange)}
.c-label{position:absolute;left:845px;color:var(--white);font-size:11px;font-weight:700}
.c-value{position:absolute;left:845px;color:#d5d5d5;font-size:11px}
.copy{left:81px;width:1026px;top:3796px;text-align:center;color:#cfcfcf;font-size:10.5px}
</style>
</head>
<body>

<!-- Hero -->
<header class="abs hero" role="img" aria-label="Photo of a laptop with a glowing security shield and padlock in a dark teal workspace"></header>
<div class="brand" style="left:203px;top:62px;font-size:24px">Emberstrata</div>
<nav class="nav"><span>HOME</span><span>ABOUT</span><span>SERVICES</span><span>CASE STUDIES</span><span>CONTACT US</span><span>BLOG</span><span>NEWS</span></nav>
<h1 class="abs hero-title">Emberstrata</h1>
<div class="abs hero-sub">Cyber Security Penetration testing</div>
<div class="btn on-dark" style="left:203px;top:365px;width:118px">GET A QUOTE</div>
<div class="abs slider-line"></div>
<span class="dot" style="left:196px"></span>
<span class="dot" style="left:212px;width:13px;height:13px;top:566px;background:var(--orange);border:2px solid var(--white)"></span>
<span class="dot" style="left:232px"></span>

<!-- About -->
<h2 class="heading" style="left:207px;top:710px">About <span>Emberstrata</span></h2>
<div class="rule" style="left:207px;top:764px"></div>
<p class="para" style="left:203px;top:785px;width:369px">Lorem ipsum dolor sit amet, consectetur adipiscing elit, sed do eiusmod tempor incididunt ut labore et dolore magna aliqua. Ut enim ad minim veniam, quis nostrud exercitation ullamco laboris nisi ut aliquip ex ea commodo consequat. Duis aute irure dolor in reprehenderit in voluptate velit esse cillum dolore eu fugiat nulla pariatur. Excepteur sint occaecat cupidatat non proident, sunt in culpa qui officia deserunt mollit anim id est laborum. Lorem ipsum dolor sit amet, consectetur adipiscing elit, sed do eiusmod tempor incididunt ut labore et dolore magna aliqua.</p>
<div class="btn" style="left:203px;top:1008px;width:118px">LEARN MORE</div>
<div class="abs" role="img" aria-label="Photo of two colleagues reviewing a laptop in a server room" style="left:684px;top:712px;width:300px;height:300px;border-radius:50%;background:radial-gradient(circle at 40% 35%,#6c7a86,#2c343c 60%,#15191d)"></div>
<div class="abs" role="img" aria-label="Photo of a man working with holographic security icons" style="left:626px;top:860px;width:184px;height:184px;border-radius:50%;border:5px solid var(--white);background:radial-gradient(circle at 50% 40%,#4a6ea8,#1d2f5c 65%,#101a36)"></div>

<!-- What we do -->
<section class="abs services" role="img" aria-label="Dark background with a faint network of connected points"></section>
<h2 class="heading light" style="left:0;width:1188px;text-align:center;top:1227px">What <span>We do</span></h2>
<div class="rule" style="left:566px;top:1282px"></div>

<div class="card-top" style="left:203px;top:1367px;width:70px"></div>
<div class="card-frame" style="left:203px;top:1367px;width:246px;height:323px"></div>
<div class="card-top" style="left:471px;top:1367px;width:70px"></div>
<div class="card-frame" style="left:471px;top:1367px;width:246px;height:323px"></div>
<div class="card-top" style="left:738px;top:1367px;width:70px"></div>
<div class="card-frame" style="left:738px;top:1367px;width:246px;height:323px"></div>

<div class="ring" style="left:271px;top:1313px"><div class="core">
<svg width="46" height="46" viewBox="0 0 46 46" fill="none" stroke="#fff" stroke-width="2"><circle cx="23" cy="23" r="19"/><circle cx="23" cy="23" r="12"/><ellipse cx="23" cy="24" rx="5" ry="7"/><path d="M23 2v8M23 36v8M2 23h8M36 23h8M18 20l-4-2M28 20l4-2M18 27l-4 2M28 27l4 2"/></svg>
</div></div>
<div class="ring" style="left:539px;top:1313px"><div class="core">
<svg width="46" height="46" viewBox="0 0 46 46" fill="none" stroke="#fff" stroke-width="2"><path d="M13 20a10 10 0 0 1 20 0v4H13z"/><rect x="9" y="24" width="28" height="16" rx="2"/><circle cx="23" cy="31" r="3"/><path d="M23 34v3"/></svg>
</div></div>
<div class="ring" style="left:806px;top:1313px"><div class="core">
<svg width="46" height="46" viewBox="0 0 46 46" fill="none" stroke="#fff" stroke-width="2"><rect x="5" y="7" width="30" height="24" rx="2"/><path d="M5 13h30M15 19l-4 3 4 3M25 19l4 3-4 3M22 17l-3 10"/><circle cx="32" cy="31" r="6"/><path d="M36 35l5 5"/></svg>
</div></div>

<span class="side-dot" style="left:443px;top:1477px"></span>
<span class="side-dot" style="left:711px;top:1477px"></span>
<span class="side-dot" style="left:978px;top:1477px"></span>

<h3 class="card-title" style="left:203px;top:1448px">Bug Bounty</h3>
<h3 class="card-title" style="left:471px;top:1448px">Penetration Testing</h3>
<h3 class="card-title" style="left:738px;top:1448px">Code Review</h3>
<p class="card-text" style="left:231px;top:1481px">Lorem ipsum dolor sit amet, consectetur adipiscing elit, sed do eiusmod tempor incididunt ut labore et dolore Lorem ipsum dolor sit amet, consectetur adipiscing elit</p>
<p class="card-text" style="left:499px;top:1481px">Lorem ipsum dolor sit amet, consectetur adipiscing elit, sed do eiusmod tempor incididunt ut labore et dolore Lorem ipsum dolor sit amet, consectetur adipiscing elit</p>
<p class="card-text" style="left:766px;top:1481px">Lorem ipsum dolor sit amet, consectetur adipiscing elit, sed do eiusmod tempor incididunt ut labore et dolore Lorem ipsum dolor sit amet, consectetur adipiscing elit</p>
<div class="btn on-dark" style="left:267px;top:1623px;width:118px">LEARN MORE</div>
<div class="btn on-dark" style="left:535px;top:1623px;width:118px">LEARN MORE</div>
<div class="btn on-dark" style="left:802px;top:1623px;width:118px">LEARN MORE</div>

<!-- Expertise -->
<div class="abs expertise-bg"></div>
<svg class="abs" style="left:81px;top:1818px" width="520" height="497" viewBox="0 0 520 497">
  <defs><linearGradient id="hackerShade" x1="0" y1="0" x2="1" y2="1"><stop offset="0" stop-color="#2b4f5e"/><stop offset=".6" stop-color="#12262f"/><stop offset="1" stop-color="#081217"/></linearGradient></defs>
  <path role="img" aria-label="Photo of a hooded figure working at several computer monitors" d="M0 0H430Q545 248 430 497H0Z" fill="url(#hackerShade)"/>
  <path d="M430 0Q545 248 430 497" fill="none" stroke="var(--orange)" stroke-width="9"/>
</svg>
<h2 class="heading" style="left:618px;top:1929px">Our <span>Expertise</span></h2>
<div class="rule" style="left:618px;top:1983px"></div>
<p class="para" style="left:615px;top:2004px;width:369px">Lorem ipsum dolor sit amet, consectetur adipiscing elit, sed do eiusmod tempor incididunt ut labore et dolore magna aliqua. Ut enim ad minim veniam, quis nostrud exercitation ullamco laboris nisi ut aliquip ex ea commodo consequat. Duis aute irure dolor in reprehenderit in voluptate velit esse cillum dolore eu fugiat nulla pariatur. Excepteur sint occaecat cupidatat non proident, sunt in culpa qui officia deserunt</p>
<div class="btn" style="left:615px;top:2165px;width:118px">LEARN MORE</div>

<!-- News -->
<h2 class="heading" style="left:0;width:1188px;text-align:center;top:2391px">News &amp; <span>Events</span></h2>
<div class="rule" style="left:566px;top:2446px"></div>
<div class="abs news-big" role="img" aria-label="Photo of a woman presenting in a security operations centre with world map screens"></div>
<div class="badge" style="left:232px;top:2732px">&#9632; 12 Apr 2023</div>
<div class="abs" style="left:233px;top:2764px;width:340px;color:var(--white);font-weight:700;font-size:14.5px;line-height:20px">Lorem ipsum dolor sit amet, consectetur adipiscing elit, sed do eiusmod</div>

<article class="news-card" style="top:2469px">
  <div class="news-thumb" role="img" aria-label="Photo of two engineers with a tablet among server racks"></div>
  <div class="badge" style="left:170px;top:20px">&#9632; 12 Apr 2023</div>
  <h3>Lorem ipsum dolor sit amet, consectetur</h3>
  <p>Lorem ipsum dolor sit amet, conse ctetur adipiscing elit, sed do eiusm od tempor incididunt</p>
</article>
<article class="news-card" style="top:2656px">
  <div class="news-thumb" role="img" aria-label="Photo of an analyst seated before several monitors"></div>
  <div class="badge" style="left:170px;top:20px">&#9632; 12 Apr 2023</div>
  <h3>Lorem ipsum dolor sit amet, consectetur</h3>
  <p>Lorem ipsum dolor sit amet, conse ctetur adipiscing elit, sed do eiusm od tempor incididunt</p>
</article>
<div class="btn" style="left:518px;top:2846px;width:153px">VIEW MORE NEWS</div>

<!-- Contact -->
<div class="abs contact-bg"></div>
<svg class="abs" style="left:630px;top:2941px" width="477" height="576" viewBox="0 0 477 576">
  <defs><linearGradient id="teamShade" x1="0" y1="0" x2="1" y2="1"><stop offset="0" stop-color="#1f3d8a"/><stop offset=".55" stop-color="#14213f"/><stop offset="1" stop-color="#0b1222"/></linearGradient></defs>
  <path role="img" aria-label="Photo of two colleagues looking at a screen in a dark office" d="M60 0H477V576H53Q-20 300 60 0Z" fill="url(#teamShade)"/>
  <path d="M60 0Q-20 300 53 576" fill="none" stroke="var(--orange)" stroke-width="9"/>
</svg>
<h2 class="heading" style="left:203px;top:3067px">Get in <span>Touch</span></h2>
<div class="rule" style="left:203px;top:3123px"></div>
<div class="field" style="left:204px;top:3151px;width:181px;height:32px">First name*</div>
<div class="field" style="left:396px;top:3151px;width:181px;height:32px">Last name*</div>
<div class="field" style="left:204px;top:3192px;width:181px;height:32px">Phone*</div>
<div class="field" style="left:396px;top:3192px;width:181px;height:32px">Email*</div>
<div class="field" style="left:204px;top:3234px;width:372px;height:94px">Message*</div>
<div class="btn" style="left:204px;top:3341px;width:153px">SEND MESSAGE</div>

<!-- Footer -->
<footer class="abs footer"></footer>
<div class="brand" style="left:203px;top:3630px;font-size:34px">Emberstrata</div>
<span class="social" style="left:242px"><i></i></span>
<span class="social" style="left:275px"><i></i></span>
<span class="social" style="left:309px"><i></i></span>
<span class="social" style="left:344px"><i></i></span>

<div class="col-head" style="left:480px">Quick Links</div>
<ul class="links" style="left:480px"><li>Home</li><li>About Us</li><li>Services</li><li>Case Studies</li><li>Contact Us</li><li>Blog</li><li>News</li></ul>
<div class="col-head" style="left:645px">Support</div>
<ul class="links" style="left:645px"><li>Careers</li><li>Support</li><li>Sitemap</li><li>Privacy policy</li><li>Terms of services</li><li>Faq</li><li>Contact us</li></ul>
<div class="col-head" style="left:811px">Contact Us</div>

<svg class="abs" style="left:811px;top:3598px" width="24" height="28" viewBox="0 0 24 28" fill="none" stroke="#fff" stroke-width="1.6"><path d="M12 26S3 16 3 10a9 9 0 0 1 18 0c0 6-9 16-9 16z"/><circle cx="12" cy="10" r="3.5"/></svg>
<div class="c-label" style="top:3596px">ADDRESS :</div>
<div class="c-value" style="top:3617px">123,Lorem ipsum dolor sit</div>
<svg class="abs" style="left:811px;top:3648px" width="26" height="26" viewBox="0 0 26 26" fill="none" stroke="#fff" stroke-width="1.6"><circle cx="13" cy="13" r="11.5"/><path d="M9 7l2 3-1.5 1.5a8 8 0 0 0 5 5L16 15l3 2-1.5 2.5C12 19 7 14 6.5 8.5z"/></svg>
<div class="c-label" style="top:3647px">PHONE :</div>
<div class="c-value" style="top:3668px">+1 888 888 8888</div>
<svg class="abs" style="left:809px;top:3700px" width="28" height="22" viewBox="0 0 28 22" fill="none" stroke="#fff" stroke-width="1.6"><rect x="1.5" y="2" width="25" height="18"/><path d="M1.5 2l12.5 11L26.5 2"/></svg>
<div class="c-label" style="top:3696px">EMAIL ADDRESS :</div>
<div class="c-value" style="top:3717px">info@companyname.com</div>

<div class="abs copy">© Copyrights 2023 Emberstrata | All Rights Reserved</div>

</body>
</html>
```